Harborline Talent IT Recruiting firm needs a business card design for Recruiters, Sourcers, and Account

We need business cards that allow us to change all contact info, names, titles (Recruiter, Sourcer, Account Manager, Director, CEO, etc) per person since we have three offices, in three cities, Phoenix, Austin, and Las Vegas. We do recruiting and contractors for IT positions (Developers, Architects, Software Engineers, Security Engineers, Help Desk, DBAs, PMs, Scrum Masters, etc.) Our client companies are very diverse from Crestline 250 to silicone Valley type start-ups.

So, while we what hip, techie, and quirky, it still needs to be professional. Primary color we use is blue, with silver as a secondary color.

Target Market(s)

IT, Technology

Industry/Entity Type

Business

Contact Information for Business Card

Company name: Harborline Talent, Inc.
Website: www.harborlinetalent-example.com
Logos for ProCircle, Quillo, and Roomwall

Name, Title, Office Number, Cell Number, email

Font styles to use
Serif
Sans Serif

Colors
0455a3
d5d5d5

Requirements
Nice to have
• The grey I selected below is not necessary - but, would like silver included. I included a card design (File 3: HTI early trial example.jpg) that I had started on. It's very rough, and not quite what we're looking for, but what we did like is the logo, big, maybe a bit faded, off center, goes out of frame, etc. Still looking for other ideas - you are the pros! But, just an idea of a design element we liked.

```html
<!DOCTYPE html>
<html lang="en">
<head>
<meta charset="utf-8">
<title>Harborline Talent — Business Card</title>
<link rel="stylesheet" href="https://fonts.googleapis.com/css2?family=Cinzel:wght@400&family=Lato:wght@400;700&display=swap">
<style>
  :root {
    --backdrop: #e9ebee;
    --blue-light: #3fb4f7;
    --blue-deep: #0455d6;
    --brand-blue: #1e88e5;
    --ink: #1b1b1b;
    --paper: #ffffff;
    --paper-shade: #ececec;
    --silver: #d5d5d5;
    --rule: #bdbdbd;
  }
  * { box-sizing: border-box; margin: 0; padding: 0; }
  html, body { width: 1200px; height: 900px; overflow: hidden; }
  body {
    background: var(--backdrop);
    position: relative;
    font-family: "Lato", Arial, sans-serif;
  }
  .card {
    position: absolute;
    width: 560px;
    height: 320px;
    border-radius: 4px;
    box-shadow: 0 10px 28px rgba(0,0,0,0.18);
    overflow: hidden;
  }

  /* Back side */
  .card-back {
    left: 50px;
    top: 110px;
    background: linear-gradient(180deg, var(--blue-light) 0%, #2a9cf3 45%, var(--blue-deep) 100%);
    color: var(--paper);
    display: flex;
    flex-direction: column;
    align-items: center;
  }
  .back-mark {
    margin-top: 42px;
    width: 150px;
    height: 150px;
    border-radius: 50%;
    background: var(--paper);
    display: flex;
    align-items: center;
    justify-content: center;
  }
  .back-mark span {
    font-family: "Cinzel", Georgia, serif;
    font-size: 17px;
    color: var(--blue-deep);
    text-align: center;
    line-height: 1.25;
  }
  .back-url {
    margin-top: 20px;
    font-size: 16px;
    letter-spacing: 0.3px;
  }
  .social-row {
    margin-top: 12px;
    display: flex;
    gap: 8px;
  }
  .social-dot {
    width: 22px;
    height: 22px;
    border-radius: 50%;
    background: var(--paper);
  }

  /* Front side */
  .card-front {
    left: 590px;
    top: 470px;
    background: radial-gradient(ellipse at 70% 30%, var(--paper) 40%, var(--paper-shade) 100%);
    color: var(--ink);
  }
  .wordmark {
    position: absolute;
    right: 30px;
    top: 34px;
    display: flex;
    align-items: center;
    gap: 10px;
  }
  .wordmark-dot {
    width: 40px;
    height: 40px;
    border-radius: 50%;
    background: var(--brand-blue);
  }
  .wordmark-name {
    font-family: "Cinzel", Georgia, serif;
    font-size: 30px;
    letter-spacing: 1px;
    color: var(--ink);
  }
  .tagline {
    position: absolute;
    right: 30px;
    top: 92px;
    font-family: "Cinzel", Georgia, serif;
    font-size: 14px;
    letter-spacing: 2px;
    color: var(--ink);
  }
  .rule {
    position: absolute;
    height: 1px;
    background: var(--rule);
  }
  .rule-top { right: 30px; top: 124px; width: 300px; }
  .rule-mid { left: 200px; top: 222px; width: 330px; }
  .contact-list {
    position: absolute;
    right: 30px;
    top: 142px;
    list-style: none;
    text-align: right;
    font-size: 14px;
    line-height: 22px;
  }
  .contact-list li {
    display: flex;
    justify-content: flex-end;
    align-items: center;
    gap: 6px;
  }
  .contact-list svg { width: 12px; height: 12px; fill: var(--brand-blue); }
  .person {
    position: absolute;
    left: 30px;
    top: 226px;
  }
  .person-name {
    font-size: 21px;
    font-weight: 700;
    color: var(--brand-blue);
    line-height: 26px;
  }
  .person-title {
    font-size: 15px;
    color: var(--ink);
    text-align: right;
    line-height: 20px;
  }
</style>
</head>
<body>

  <section class="card card-back">
    <div class="back-mark"><span>Harborline<br>Talent</span></div>
    <p class="back-url">www.harborlinetalent-example.com</p>
    <div class="social-row" aria-label="Social profiles: Roomwall, Quillo, ProCircle">
      <span class="social-dot"></span>
      <span class="social-dot"></span>
      <span class="social-dot"></span>
    </div>
  </section>

  <section class="card card-front">
    <div class="wordmark">
      <span class="wordmark-name">HARBORLINE TALENT</span>
      <span class="wordmark-dot"></span>
    </div>
    <p class="tagline">Built for the Next Move</p>
    <div class="rule rule-top"></div>

    <ul class="contact-list">
      <li>555 014-2290
        <svg viewBox="0 0 12 12" aria-label="Office"><path d="M1 4c0-1.5 2.5-2.5 5-2.5S11 2.5 11 4v1H8.5V4h-5v1H1zM3 6h6l1.5 4.5h-9z"/></svg>
      </li>
      <li>555 014-2290
        <svg viewBox="0 0 12 12" aria-label="Cell"><path d="M3.5 0.5h5a1 1 0 0 1 1 1v9a1 1 0 0 1-1 1h-5a1 1 0 0 1-1-1v-9a1 1 0 0 1 1-1zM4 2v7h4V2z"/></svg>
      </li>
      <li>info@harborlinetalent-example.com
        <svg viewBox="0 0 12 12" aria-label="Email"><path d="M0.5 2h11v8h-11zM1.5 3l4.5 3.5L10.5 3z" fill-rule="evenodd"/></svg>
      </li>
    </ul>

    <div class="rule rule-mid"></div>
    <div class="person">
      <p class="person-name">Jordan Avery K</p>
      <p class="person-title">Designation</p>
    </div>
  </section>

</body>
</html>
```